Women's health flyer for Vindmark Health & Wellness . for a Women's health conference

I need a flyer , post card 4x 6 or 5 x 7 sized designed , 2 sides focused on my business branding and Women's health. we deliver bespoke care and focus on all phases of women's health and life. I want something aligned with our bespoke whole person care philosophy and that is fresh and forward thinking.
www.vindmark-care.com
This is to help women know they can have care for all phases of life , fertility , postpartum , perimenopause , mental health , wellness, weight loss, increased energy stress , menopause etc
please use knowledge from website about my company , www.vindmark-care.com
I also feel like my brand kit could use an additional secondarily color option in it

Target Market(s)

Women 25-70

Industry/Entity Type

health & Wellness

Colors
0054AA
0677BA
7BADD7
CADEEF
E8F1F8
0094D4
00A9DD
6FCCEA
C7EBF8
E9F6FB
00AB8E
00BBA5
67D7C9
C6EFE9
E9F9F6
59FF00
82FF00
B8FF75
E3FFCB
F4FFEA
E54698
E96AAD
F1A4CE
F9D9EA
FCEFF6
A7469A
B969AE
D3A5CF
EDDBEB
F8F0F9

Requirements
Must have
• photos , my logo, connection to my brand
Nice to have
• something fresh and different
Should not have
• look like a genetic "wellness program"

```html
<!DOCTYPE html>
<html lang="en">
<head>
<meta charset="utf-8">
<title>Vindmark Health &amp; Wellness – Postcard</title>
<link rel="stylesheet" href="https://fonts.googleapis.com/css2?family=Cinzel:wght@400;500&family=Montserrat:wght@400;500;600&family=Arimo:ital,wght@0,400;0,700;1,700&display=swap">
<style>
:root{
  --stage:#2e2e2e;
  --white:#ffffff;
  --ink:#1c1c1c;
  --navy:#16607e;
  --teal-dark:#137090;
  --teal:#1e8fb0;
  --cyan:#2bb0e0;
  --green:#6aba2a;
  --green-bright:#7cc242;
  --btn-3:#1a86a8;
  --btn-4:#177b9c;
  --btn-5:#0f6884;
}
*{box-sizing:border-box;margin:0;padding:0}
html,body{width:1200px;height:1200px;overflow:hidden;background:var(--stage)}
.card{position:absolute;left:254px;width:731px;height:522px;background:var(--white);overflow:hidden;font-family:"Arimo",Arial,sans-serif;color:var(--ink)}
.card--front{top:64px}
.card--back{top:617px}
.card svg.backdrop{position:absolute;inset:0}

/* front */
.brand{position:absolute;left:440px;top:66px;width:280px;text-align:center;color:var(--navy);font-family:"Montserrat",sans-serif;font-weight:600}
.brand__mark{display:block;width:40px;height:40px;border-radius:50%;background:var(--cyan);margin:0 auto 10px}
.brand__name{font-size:38px;letter-spacing:1px;line-height:1}
.brand__sub{font-size:11px;letter-spacing:3px;margin-top:4px}
.headline{position:absolute;left:400px;top:208px;width:360px;text-align:center}
.headline__top{font-family:"Cinzel",serif;font-size:34px;color:var(--teal-dark);line-height:1.05}
.headline__bottom{font-family:"Montserrat",sans-serif;font-size:24px;letter-spacing:5px;color:var(--green);margin-top:4px}
.headline__bottom i{display:inline-block;width:6px;height:6px;border-radius:50%;background:var(--cyan);vertical-align:middle;margin:0 6px}
.intro{position:absolute;left:22px;top:312px;width:366px;font-size:15.4px;line-height:18px;text-align:justify}
.intro strong{color:var(--teal)}
.intro__cta{margin-top:6px;color:var(--teal);font-weight:700;font-style:italic}
.services{position:absolute;left:14px;top:444px;display:flex;gap:10px}
.service{height:61px;border-radius:8px;border:2px solid var(--white);box-shadow:0 0 0 1px rgba(0,0,0,.08);color:var(--white);font-family:"Montserrat",sans-serif;font-weight:500;font-size:13.2px;line-height:15px;display:flex;align-items:center;justify-content:center;text-align:center;text-transform:uppercase;padding:0 6px}
.service--corporate{width:133px;background:var(--green)}
.service--coaching{width:132px;background:var(--cyan)}
.service--retreats{width:134px;background:var(--btn-3)}
.service--workshops{width:132px;background:var(--btn-4)}
.service--tem{width:135px;background:var(--btn-5);font-size:11.6px;line-height:13px}

/* back */
.name-bar{position:absolute;left:0;top:17px;width:442px;height:30px;background:var(--teal-dark);border-radius:0 15px 15px 0;color:var(--white);font-family:"Cinzel",serif;font-size:21px;line-height:30px;padding-left:30px;white-space:nowrap}
.bio{position:absolute;left:34px;top:62px;width:402px;font-size:15px;line-height:17.6px;text-align:justify;hyphens:auto}
.pillars{position:absolute;left:240px;top:260px;list-style:none;font-family:"Montserrat",sans-serif;font-weight:500;font-size:14.4px;line-height:18px;color:var(--navy)}
.pillars li{position:relative;padding-left:14px}
.pillars li::before{content:"";position:absolute;left:0;top:7px;width:5px;height:5px;border-radius:50%;background:var(--green)}
.contact{position:absolute;left:20px;top:466px;list-style:none;font-size:13px;line-height:18px}
.contact li{display:flex;align-items:center;gap:6px;white-space:nowrap}
.contact svg{width:11px;height:11px;fill:var(--green)}
.web-pill{position:absolute;left:236px;top:496px;width:152px;height:21px;border-radius:11px;background:var(--green-bright);color:var(--white);font-family:"Montserrat",sans-serif;font-weight:600;font-size:13px;line-height:21px;text-align:center;white-space:nowrap}
</style>
</head>
<body>

<section class="card card--front">
  <svg class="backdrop" width="731" height="522" viewBox="0 0 731 522">
    <defs>
      <linearGradient id="sky-fade" x1="0" y1="0" x2="0" y2="1">
        <stop offset="0" stop-color="#ffffff" stop-opacity="0"/>
        <stop offset="1" stop-color="#6fccea"/>
      </linearGradient>
      <linearGradient id="beach" x1="0" y1="0" x2="0" y2="1">
        <stop offset="0" stop-color="#c9d3e2"/>
        <stop offset=".55" stop-color="#e9d9d2"/>
        <stop offset="1" stop-color="#a9a8b0"/>
      </linearGradient>
      <linearGradient id="boardwalk" x1="0" y1="0" x2="0" y2="1">
        <stop offset="0" stop-color="#7fb4e6"/><stop offset="1" stop-color="#5f7d55"/>
      </linearGradient>
      <linearGradient id="jetty" x1="0" y1="0" x2="0" y2="1">
        <stop offset="0" stop-color="#8a9aa4"/><stop offset=".55" stop-color="#76b8b4"/><stop offset="1" stop-color="#b98b62"/>
      </linearGradient>
    </defs>
    <path d="M731 240 C600 270 520 330 420 420 L360 522 H731 Z" fill="url(#sky-fade)" opacity=".85"/>
    <path d="M0 0 H731 V30 A306 306 0 0 0 362 207 C300 270 200 300 120 290 C70 283 30 260 0 235 Z" fill="url(#beach)" role="img" aria-label="Photo of a woman holding a yoga warrior pose on a beach at sunset"/>
    <path d="M372 196 A306 306 0 0 1 731 36" fill="none" stroke="#2bb0e0" stroke-width="12"/>
    <circle cx="502" cy="364" r="62" fill="url(#boardwalk)" stroke="#6aba2a" stroke-width="3" role="img" aria-label="Photo of a wooden boardwalk crossing a lake under a blue sky"/>
    <circle cx="646" cy="364" r="62" fill="url(#jetty)" stroke="#6aba2a" stroke-width="3" role="img" aria-label="Photo of a stone jetty leading into a calm sea"/>
  </svg>

  <div class="brand">
    <span class="brand__mark"></span>
    <div class="brand__name">VINDMARK</div>
    <div class="brand__sub">HEALTH &amp; WELLNESS</div>
  </div>

  <div class="headline">
    <div class="headline__top">BESPOKE WHOLE</div>
    <div class="headline__bottom"><i></i>PERSON CARE<i></i></div>
  </div>

  <div class="intro">
    <p>Embark on this transformative journey of holistic women’s healing with <strong>DR MAREN L OSTBY DACM, L.AC.,</strong> where art, science, and compassion converge to forge a healthier, happier community.</p>
    <p class="intro__cta">Let’s explore the profound potential of Bespoke Whole Person Care together!</p>
  </div>

  <div class="services">
    <div class="service service--corporate">Customized Corporate Wellness</div>
    <div class="service service--coaching">Individual Coaching</div>
    <div class="service service--retreats">Retreats</div>
    <div class="service service--workshops">Workshops</div>
    <div class="service service--tem">Acupuncture &amp; Traditional East Asian Medicine</div>
  </div>
</section>

<section class="card card--back">
  <svg class="backdrop" width="731" height="522" viewBox="0 0 731 522">
    <defs>
      <linearGradient id="back-fade" x1="0" y1="0" x2="0" y2="1">
        <stop offset="0" stop-color="#ffffff"/>
        <stop offset=".4" stop-color="#d9f1fa"/>
        <stop offset="1" stop-color="#5cc4e8"/>
      </linearGradient>
      <linearGradient id="portrait" x1="0" y1="0" x2="0" y2="1">
        <stop offset="0" stop-color="#9a9a9a"/><stop offset="1" stop-color="#3d3d3d"/>
      </linearGradient>
    </defs>
    <path d="M0 236 C150 250 300 245 480 236 L480 522 H0 Z" fill="url(#back-fade)"/>
    <path d="M0 446 C120 474 260 474 400 446 L480 434 V522 H0 Z" fill="#ffffff"/>
    <path d="M490 0 C512 130 510 240 475 330 C452 395 458 460 478 522 H731 V0 Z" fill="#ffffff"/>
    <path d="M463 0 C478 120 470 230 430 320 C405 390 415 460 436 522 H455 C435 460 430 390 455 320 C495 230 498 130 478 0 Z" fill="#2bb0e0"/>
    <path d="M478 0 C498 130 495 230 455 320 C430 390 435 460 455 522 H478 C458 460 452 395 475 330 C510 240 512 130 490 0 Z" fill="#137090"/>
    <circle cx="114" cy="307" r="55" fill="url(#portrait)" stroke="#6aba2a" stroke-width="3" role="img" aria-label="Black and white portrait photo of the practitioner"/>
  </svg>

  <div class="name-bar">DR MAREN L OSTBY DACM, L.AC.,</div>

  <p class="bio">I earned a Master’s degree in Oriental Medicine from Lakeshore Health Sciences University and a Doctorate from Coastal College of Health &amp; Sciences., both with honors. With over a decade of dedicated practice, I realized early on that T.E.A.M transcends acupuncture needles—it fosters a lifestyle of connection and self- awareness. This realization compelled me to extend my impact beyond clinical settings, developing innovative programs that enrich and uplift my community under the umbrella of Vindmark Health &amp; Wellness.</p>

  <ul class="pillars">
    <li>WHOLE PERSON<br>APPROACH</li>
    <li>REVOLUTIONARY<br>DESIGNED<br>PROGRAMS</li>
    <li>COMPREHENSIVE<br>SUPPORT</li>
    <li>COMMUNITY AND<br>INDIVIDUALITY</li>
  </ul>

  <ul class="contact">
    <li><svg viewBox="0 0 12 12"><path d="M6 0a4 4 0 0 0-4 4c0 3 4 8 4 8s4-5 4-8a4 4 0 0 0-4-4zm0 5.6A1.6 1.6 0 1 1 6 2.4a1.6 1.6 0 0 1 0 3.2z"/></svg>1420 Larkspur Ave Fairview, MO, 64000</li>
    <li><svg viewBox="0 0 12 12"><path d="M2.6 0.6 4.4 2.8 3.4 4.4c.8 1.6 2.2 3 3.8 3.8l1.6-1 2.2 1.8-1 2.2C5 11 1 7 0.4 1.6z"/></svg>+1-555-014-2277</li>
    <li><svg viewBox="0 0 12 12"><path d="M0 2h12v1L6 7 0 3zM0 4.4 6 8.4l6-4V10H0z"/></svg>maren@marenostby.com</li>
  </ul>

  <div class="web-pill">vindmark-care.com</div>
</section>

</body>
</html>
```